VELMOTIK Amazing Business Cards Challenge

Velmoti is a new technology company that will provide engineering and manufacturing services in the electric vehicle industry.

We are looking at a new business card that will support our orientation in providing advanced, innovative solutions. The business card will be lean and present the only information required to be more efficient.

Target Market(s)

Fleet operators, private commercial vehicle operators, delivery companies.

Industry/Entity Type

Business

Contact Information for Business Card

Use the logo and its colors, use a white background.

Font styles to use
Sans Serif

Colors
0455a3
ffffff
9bcb3c

Requirements
Must have
• Velmotik Logo
• All informations in the DOC file = 3 different cards.
• White background
Nice to have
• Icons for email, phone and web address.
• Cute design and strong identity.
Should not have
• Bleeds

```html
<!DOCTYPE html>
<html lang="fr">
<head>
<meta charset="utf-8">
<title>Velmotik – Business Cards</title>
<link href="https://fonts.googleapis.com/css2?family=Open+Sans:wght@400;600;700&display=swap" rel="stylesheet">
<style>
  :root {
    --bg: #6b6b6b;
    --card: #ffffff;
    --brand-blue: #0a6fb8;
    --ink-strong: #333333;
    --ink: #555555;
    --wordmark: #4a4a4a;
    --pattern: #ececec;
  }
  * { box-sizing: border-box; margin: 0; padding: 0; }
  html, body { width: 900px; height: 1200px; overflow: hidden; }
  body {
    background: var(--bg);
    font-family: "Open Sans", Arial, sans-serif;
    position: relative;
  }
  .card {
    position: absolute;
    left: 169px;
    width: 562px;
    height: 316px;
    background: var(--card);
  }
  .card--ceo { top: 90px; }
  .card--bizdev { top: 441px; }
  .card--ops { top: 795px; }

  .pattern-band {
    position: absolute;
    left: 8px;
    right: 8px;
    height: 48px;
    background: var(--pattern);
    border-radius: 2px;
  }
  .pattern-band--top { top: 6px; }
  .pattern-band--bottom { bottom: 8px; }

  .brand {
    position: absolute;
    left: 46px;
    width: 180px;
    top: 118px;
    display: flex;
    flex-direction: column;
    align-items: center;
  }
  .brand__dot {
    width: 44px;
    height: 44px;
    border-radius: 50%;
    background: var(--brand-blue);
  }
  .brand__name {
    margin-top: 8px;
    font-size: 34px;
    font-weight: 600;
    line-height: 1;
    color: var(--wordmark);
    letter-spacing: 1px;
  }

  .contact {
    position: absolute;
    left: 319px;
    font-size: 12px;
    line-height: 18px;
    color: var(--ink);
  }
  .contact__name { font-weight: 700; color: var(--ink-strong); font-size: 12.5px; }
  .contact__role--strong { font-weight: 700; color: var(--ink-strong); }
  .contact__address { margin-top: 22px; }
  .contact__list { list-style: none; margin-top: 4px; }
  .contact__item { display: flex; align-items: center; height: 22px; }
  .contact__icon { width: 14px; height: 14px; margin-right: 6px; flex: none; }

  .card--ceo .contact { top: 76px; }
  .card--bizdev .contact { top: 68px; }
  .card--ops .contact { top: 70px; }
  .card--ops .contact__address { margin-top: 36px; }
</style>
</head>
<body>

<svg width="0" height="0" style="position:absolute">
  <defs>
    <symbol id="icon-phone" viewBox="0 0 14 14">
      <circle cx="7" cy="7" r="7" fill="#0a6fb8"/>
      <rect x="4.5" y="3" width="5" height="8" rx="1" fill="none" stroke="#fff" stroke-width="1.2"/>
      <line x1="6" y1="9.5" x2="8" y2="9.5" stroke="#fff" stroke-width="1"/>
    </symbol>
    <symbol id="icon-mail" viewBox="0 0 14 14">
      <circle cx="7" cy="7" r="7" fill="#0a6fb8"/>
      <rect x="3.5" y="4.5" width="7" height="5" fill="#fff"/>
      <polyline points="3.5,4.5 7,7.5 10.5,4.5" fill="none" stroke="#0a6fb8" stroke-width="0.9"/>
    </symbol>
    <symbol id="icon-web" viewBox="0 0 14 14">
      <circle cx="7" cy="7" r="7" fill="#0a6fb8"/>
      <circle cx="7" cy="7" r="4" fill="none" stroke="#fff" stroke-width="1"/>
      <ellipse cx="7" cy="7" rx="1.8" ry="4" fill="none" stroke="#fff" stroke-width="0.8"/>
      <line x1="3" y1="7" x2="11" y2="7" stroke="#fff" stroke-width="0.8"/>
    </symbol>
  </defs>
</svg>

<!-- Card: President -->
<section class="card card--ceo">
  <div class="pattern-band pattern-band--top" role="img" aria-label="Faint repeating brand pattern band"></div>
  <div class="brand">
    <span class="brand__dot"></span>
    <span class="brand__name">velmotik</span>
  </div>
  <div class="contact">
    <p class="contact__name">Mathieu Bérubé, ing., M.Sc.A.</p>
    <p class="contact__role">Président | CEO</p>
    <p class="contact__address">410 – 218 Laurier Ouest,<br>Montréal (Québec) H2T 2N7 Canada</p>
    <ul class="contact__list">
      <li class="contact__item"><svg class="contact__icon"><use href="#icon-phone"/></svg>+1 514 555 0142</li>
      <li class="contact__item"><svg class="contact__icon"><use href="#icon-mail"/></svg>mberube@velmotik.com</li>
      <li class="contact__item"><svg class="contact__icon"><use href="#icon-web"/></svg>velmotik.com</li>
    </ul>
  </div>
  <div class="pattern-band pattern-band--bottom" role="img" aria-label="Faint repeating brand pattern band"></div>
</section>

<!-- Card: VP Business Development -->
<section class="card card--bizdev">
  <div class="pattern-band pattern-band--top" role="img" aria-label="Faint repeating brand pattern band"></div>
  <div class="brand">
    <span class="brand__dot"></span>
    <span class="brand__name">velmotik</span>
  </div>
  <div class="contact">
    <p class="contact__name">Olivier Dufresne</p>
    <p class="contact__role">V.P. Développement des affaires</p>
    <p class="contact__role">V.P. Business Development</p>
    <p class="contact__address" style="margin-top:20px">410 – 218 Laurier Ouest,<br>Montréal (Québec) H2T 2N7 Canada</p>
    <ul class="contact__list">
      <li class="contact__item"><svg class="contact__icon"><use href="#icon-phone"/></svg>+1 514 555 0187</li>
      <li class="contact__item"><svg class="contact__icon"><use href="#icon-mail"/></svg>odufresne@velmotik.com</li>
      <li class="contact__item"><svg class="contact__icon"><use href="#icon-web"/></svg>velmotik.com</li>
    </ul>
  </div>
  <div class="pattern-band pattern-band--bottom" role="img" aria-label="Faint repeating brand pattern band"></div>
</section>

<!-- Card: VP Operations -->
<section class="card card--ops">
  <div class="pattern-band pattern-band--top" role="img" aria-label="Faint repeating brand pattern band"></div>
  <div class="brand">
    <span class="brand__dot"></span>
    <span class="brand__name">velmotik</span>
  </div>
  <div class="contact">
    <p class="contact__name">Gilles Thériault</p>
    <p class="contact__role contact__role--strong">V.P. Opérations | V.P. Operations</p>
    <p class="contact__address">410 – 218 Laurier Ouest,<br>Montréal (Québec) H2T 2N7 Canada</p>
    <ul class="contact__list">
      <li class="contact__item"><svg class="contact__icon"><use href="#icon-phone"/></svg>+1 514 555 0163</li>
      <li class="contact__item"><svg class="contact__icon"><use href="#icon-mail"/></svg>gtheriault@velmotik.com</li>
      <li class="contact__item"><svg class="contact__icon"><use href="#icon-web"/></svg>velmotik.com</li>
    </ul>
  </div>
  <div class="pattern-band pattern-band--bottom" role="img" aria-label="Faint repeating brand pattern band"></div>
</section>

</body>
</html>
```